Dental Medical History Form - Content provided

Design a medical history form for a dental practice. Content is provided so all that is needed is the formatting to make it look great and easy to read.

"Patient Information" to include all information contained in top portion of the "Patient Medical History Form" docx file.

"Medical History" should follow the formatting and content of the "Exact Medical History" file as this is what the entry fields look like in our practice software and so we would like it to match.

1st page - Patient info, allergies, medications, antibiotics, joint replacement, pregnancy.

2nd page - Do you have, or have you had, any of the following? . . . . . . .
Updates

Project Deadline Extended Reason: Picked too short of a deadline to start (2 days) Added Monday, February 13, 2017

Target Market(s)

All ages but must be clear enough for elderly to read. Use as much space as possible to keep font size bigger yet keep to two pages

Industry/Entity Type

Dental

Font styles to use
Sans Serif

Requirements
Must have
• All content provided
• Our logo at the top (file provided)
• Century Gothic Font
• Limit to two pages

```html
<!DOCTYPE html>
<html lang="en">
<head>
<meta charset="utf-8">
<title>Harbourline Dental – Confidential Medical History</title>
<link rel="stylesheet" href="https://fonts.googleapis.com/css2?family=Questrial&display=swap">
<style>
  :root{
    --backdrop:#e6e5e3;
    --paper:#ffffff;
    --ink:#2a2a2a;
    --muted:#6a6a6a;
    --rule:#555555;
    --band-1:#5b5b5e;
    --band-2:#9b9b9b;
    --band-3:#c9c1b9;
    --band-4:#dedddb;
  }
  *{box-sizing:border-box;margin:0;padding:0}
  html,body{width:1200px;height:927px;overflow:hidden}
  body{background:var(--backdrop);font-family:"Questrial",sans-serif;color:var(--ink);position:relative}

  .page{position:absolute;width:476px;height:672px;background:var(--paper);box-shadow:0 2px 8px rgba(0,0,0,.12)}
  .page--patient{left:94px;top:70px}
  .page--history{left:623px;top:162px}

  .band{position:absolute;left:0;right:0;height:6px;display:flex}
  .band--top{top:0}.band--bottom{bottom:0}
  .band span{flex:1}
  .band span:nth-child(1){background:var(--band-1)}
  .band span:nth-child(2){background:var(--band-2)}
  .band span:nth-child(3){background:var(--band-3)}
  .band span:nth-child(4){background:var(--band-4)}

  .brand{position:absolute;display:flex;align-items:center;gap:6px;color:var(--muted);font-size:25px;letter-spacing:.3px}
  .brand i{display:block;width:9px;height:9px;border-radius:50%;background:var(--band-2)}

  .practice-address{position:absolute;right:29px;top:30px;text-align:right;font-size:7px;line-height:9.5px}

  .form-title{position:absolute;left:0;right:0;top:94px;text-align:center;font-size:16px;font-weight:700;letter-spacing:.3px}

  .abs{position:absolute}
  .txt{font-size:8.5px;white-space:nowrap}
  .heading{font-size:9px;font-weight:700;white-space:nowrap}
  .caption{font-size:6px;font-style:italic;color:var(--muted)}

  .field{display:flex;align-items:flex-end;font-size:8.5px;height:12.6px;white-space:nowrap}
  .field .line{flex:1;border-bottom:1px solid var(--rule);margin-left:2px;height:8px}
  .field .line.short{flex:none}

  .box{display:inline-block;width:8px;height:8px;border:1px solid var(--rule);background:#fff;vertical-align:middle}
  .tick{display:inline-block;width:14px;height:12px;vertical-align:-2px}

  .write-line{position:absolute;height:0;border-bottom:1px solid var(--rule)}

  .turnover{position:absolute;right:40px;top:646px;font-size:9px;font-weight:700;font-style:italic}

  /* page two */
  .question{position:absolute;left:22px;top:78px;font-size:9.5px}
  .group{position:absolute}
  .group--left{left:22px;--yes:172px;--ybox:192px;--no:208px;--nbox:224px}
  .group--right{left:270px;--yes:121px;--ybox:140px;--no:157px;--nbox:173px}
  .group h3{font-size:8.5px;font-weight:700;height:10.4px;line-height:10.4px}
  .row{position:relative;height:10.4px;line-height:10.4px;font-size:8.5px;white-space:nowrap}
  .row .y{position:absolute;left:var(--yes)}
  .row .yb{position:absolute;left:var(--ybox);top:1px}
  .row .n{position:absolute;left:var(--no)}
  .row .nb{position:absolute;left:var(--nbox);top:1px}

  .thanks{position:absolute;left:0;right:0;top:628px;text-align:center;font-size:6.8px;font-style:italic;line-height:9px}
</style>
</head>
<body>

<!-- Page one: patient information -->
<section class="page page--patient">
  <div class="band band--top"><span></span><span></span><span></span><span></span></div>

  <div class="brand" style="left:30px;top:24px">Harbourline Dental <i></i></div>
  <address class="practice-address" style="font-style:normal">
    Harbourline Dental<br>Suite 4/18 Bayview Rd<br>Tarrin NSW 2261<br>(02) 4391 5520
  </address>

  <h1 class="form-title">CONFIDENTIAL MEDICAL HISTORY</h1>

  <!-- Patient details -->
  <div class="abs" style="left:30px;top:132px;width:209px">
    <div class="field">Name:<span class="line"></span></div>
    <div class="caption" style="position:relative;height:9px">
      <span class="abs" style="left:37px">Title</span><span class="abs" style="left:80px">First</span>
      <span class="abs" style="left:114px">Middle</span><span class="abs" style="left:167px">Last</span>
    </div>
    <div class="field">Address:<span class="line"></span></div>
    <div class="field">DOB:<span class="line short" style="width:130px"></span></div>
    <div class="field">Email Address:<span class="line"></span></div>
    <div class="field">Phone Number(s):<span class="line"></span></div>
    <div class="caption" style="position:relative;height:9px">
      <span class="abs" style="left:91px">Mobile</span><span class="abs" style="left:134px">Work</span>
      <span class="abs" style="left:172px">Home</span>
    </div>
  </div>

  <div class="abs" style="left:30px;top:234px;width:205px">
    <div class="heading" style="height:12px">Emergency Contact Person:</div>
    <div class="field">Name:<span class="line"></span></div>
    <div class="field">Relationship:<span class="line"></span></div>
    <div class="field">Phone number:<span class="line"></span></div>
  </div>

  <!-- GP and health fund -->
  <div class="abs" style="left:250px;top:135px;width:198px">
    <div class="heading" style="height:11px">General Practitioner:</div>
    <div class="field">Name:<span class="line"></span></div>
    <div class="field">Practice Name:<span class="line"></span></div>
    <div class="field">Phone Number:<span class="line"></span></div>
  </div>
  <div class="abs txt" style="left:250px;top:195px">Do you have a health fund with dental cover?</div>
  <div class="abs txt" style="left:314px;top:208px"><span class="box"></span> Yes &nbsp;or <span class="box"></span>No</div>
  <div class="abs" style="left:250px;top:219px;width:198px">
    <div class="field">If so, what is the name of the fund?<span class="line"></span></div>
    <div class="field">Fund Number?<span class="line"></span></div>
    <div class="field">Priority Number on card: 0 &nbsp;1 &nbsp;2 &nbsp;3 &nbsp;4 &nbsp;&nbsp;5</div>
  </div>
  <div class="abs" style="left:250px;top:266px;width:188px">
    <div class="field">Occupation:<span class="line"></span></div>
    <div class="field">Referred by:<span class="line"></span></div>
  </div>

  <!-- Allergies -->
  <div class="abs heading" style="left:30px;top:315px">Please indicate if &nbsp;you are allergic to any of the following
    <svg class="tick" viewBox="0 0 14 12" aria-hidden="true"><rect x="0.5" y="1.5" width="10" height="10" fill="none" stroke="#333"/><path d="M2 6l3 4 8-9" fill="none" stroke="#222" stroke-width="1.4"/></svg> ?</div>
  <div class="abs txt" style="left:30px;top:334px">Aspirin</div><span class="abs box" style="left:105px;top:336px"></span>
  <div class="abs txt" style="left:130px;top:334px">Codeine</div><span class="abs box" style="left:171px;top:335px"></span>
  <div class="abs txt" style="left:194px;top:334px">Penicillin</div><span class="abs box" style="left:238px;top:335px"></span>
  <div class="abs txt" style="left:263px;top:334px">Sulfites</div><span class="abs box" style="left:295px;top:336px"></span>
  <div class="abs txt" style="left:30px;top:350px">Local Anaesthetic</div><span class="abs box" style="left:105px;top:353px"></span>
  <div class="abs txt" style="left:130px;top:350px">Lactose</div><span class="abs box" style="left:171px;top:352px"></span>
  <div class="abs txt" style="left:194px;top:350px">Nickel</div><span class="abs box" style="left:238px;top:352px"></span>
  <div class="abs txt" style="left:263px;top:350px">Latex</div><span class="abs box" style="left:295px;top:353px"></span>
  <div class="abs" style="left:30px;top:365px;width:447px"><div class="field">Other:<span class="line"></span></div></div>

  <!-- Medications -->
  <div class="abs heading" style="left:30px;top:393px">Are you currently taking, or have ever taken, any of the following medication
    <svg class="tick" viewBox="0 0 14 12" aria-hidden="true"><rect x="0.5" y="1.5" width="10" height="10" fill="none" stroke="#333"/><path d="M2 6l3 4 8-9" fill="none" stroke="#222" stroke-width="1.4"/></svg> ?</div>
  <div class="abs txt" style="left:29px;top:410px">Asthma inhaler</div><span class="abs box" style="left:116px;top:412px"></span>
  <div class="abs txt" style="left:146px;top:410px">Anti-epileptics</div><span class="abs box" style="left:220px;top:412px"></span>
  <div class="abs txt" style="left:259px;top:410px">Anti-depressants</div><span class="abs box" style="left:338px;top:412px"></span>
  <div class="abs txt" style="left:377px;top:410px">Blood Pressure</div><span class="abs box" style="left:434px;top:412px"></span>
  <div class="abs txt" style="left:29px;top:426px">Blood Thinners</div><span class="abs box" style="left:116px;top:428px"></span>
  <div class="abs txt" style="left:146px;top:426px">Bisphosphonates</div><span class="abs box" style="left:220px;top:428px"></span>
  <div class="abs txt" style="left:259px;top:426px">Chemotherapy</div><span class="abs box" style="left:338px;top:428px"></span>
  <div class="abs txt" style="left:377px;top:426px">Insulin</div><span class="abs box" style="left:434px;top:428px"></span>
  <div class="abs txt" style="left:29px;top:442px">Immunosuppressants</div><span class="abs box" style="left:116px;top:444px"></span>
  <div class="abs txt" style="left:146px;top:442px">Steroids</div><span class="abs box" style="left:220px;top:444px"></span>
  <div class="abs txt" style="left:259px;top:442px">Oral Contraceptive</div><span class="abs box" style="left:338px;top:444px"></span>
  <div class="abs txt" style="left:377px;top:442px">Other</div><span class="abs box" style="left:434px;top:444px"></span>

  <div class="abs heading" style="left:28px;top:462px">Please specify medication name, dose, and frequency where possible:</div>
  <span class="write-line" style="left:30px;width:129px;top:488px"></span>
  <span class="write-line" style="left:174px;width:128px;top:488px"></span>
  <span class="write-line" style="left:317px;width:128px;top:488px"></span>
  <span class="write-line" style="left:30px;width:129px;top:506px"></span>
  <span class="write-line" style="left:174px;width:128px;top:506px"></span>
  <span class="write-line" style="left:317px;width:128px;top:506px"></span>
  <span class="write-line" style="left:30px;width:129px;top:524px"></span>
  <span class="write-line" style="left:174px;width:128px;top:524px"></span>
  <span class="write-line" style="left:317px;width:128px;top:524px"></span>

  <!-- Antibiotics and joints -->
  <div class="abs heading" style="left:31px;top:537px">Do you require antibiotic cover?</div>
  <div class="abs txt" style="left:203px;top:538px">Yes</div><span class="abs box" style="left:224px;top:540px"></span>
  <div class="abs txt" style="left:241px;top:538px">No</div><span class="abs box" style="left:258px;top:540px"></span>
  <div class="abs heading" style="left:31px;top:555px">Have you had a joint replacement?</div>
  <div class="abs txt" style="left:203px;top:556px">Yes</div><span class="abs box" style="left:224px;top:558px"></span>
  <div class="abs txt" style="left:241px;top:556px">No</div><span class="abs box" style="left:258px;top:558px"></span>

  <!-- Women -->
  <div class="abs heading" style="left:31px;top:578px">Women:</div>
  <div class="abs heading" style="left:31px;top:593px">Are you pregnant?</div>
  <div class="abs txt" style="left:126px;top:594px">Yes</div><span class="abs box" style="left:150px;top:596px"></span>
  <div class="abs txt" style="left:170px;top:594px">No</div><span class="abs box" style="left:189px;top:596px"></span>
  <div class="abs txt" style="left:214px;top:594px">Possible</div><span class="abs box" style="left:253px;top:596px"></span>
  <div class="abs txt" style="left:274px;top:594px">or</div>
  <div class="abs heading" style="left:31px;top:609px">Breast Feeding?</div>
  <div class="abs txt" style="left:126px;top:610px">Yes</div><span class="abs box" style="left:150px;top:612px"></span>
  <div class="abs txt" style="left:170px;top:610px">No</div><span class="abs box" style="left:189px;top:612px"></span>

  <div class="turnover">Please Turnover</div>

  <div class="band band--bottom"><span></span><span></span><span></span><span></span></div>
</section>

<!-- Page two: medical history -->
<section class="page page--history">
  <div class="band band--top"><span></span><span></span><span></span><span></span></div>

  <div class="brand" style="left:29px;top:28px">Harbourline Dental <i></i></div>
  <p class="question">Do you have, or have you had, any of the following?</p>

  <div class="group group--left" style="top:99px">
    <h3>Dental</h3>
    <div class="row">Acid Reflux<span class="y">Yes</span><span class="box yb"></span><span class="n">No</span><span class="box nb"></span></div>
    <div class="row">Bad Breath/Taste<span class="y">Yes</span><span class="box yb"></span><span class="n">No</span><span class="box nb"></span></div>
    <div class="row">Bleeding/Swollen/Sore Gums<span class="y">Yes</span><span class="box yb"></span><span class="n">No</span><span class="box nb"></span></div>
    <div class="row">Blisters/Ulcers in Mouth<span class="y">Yes</span><span class="box yb"></span><span class="n">No</span><span class="box nb"></span></div>
    <div class="row">Broken tooth/filling<span class="y">Yes</span><span class="box yb"></span><span class="n">No</span><span class="box nb"></span></div>
    <div class="row">Burning tongue<span class="y">Yes</span><span class="box yb"></span><span class="n">No</span><span class="box nb"></span></div>
    <div class="row">Dry mouth<span class="y">Yes</span><span class="box yb"></span><span class="n">No</span><span class="box nb"></span></div>
    <div class="row">Food collection between teeth<span class="y">Yes</span><span class="box yb"></span><span class="n">No</span><span class="box nb"></span></div>
    <div class="row">Grinding/clenching teeth (day/night)<span class="y">Yes</span><span class="box yb"></span><span class="n">No</span><span class="box nb"></span></div>
    <div class="row">Loose teeth<span class="y">Yes</span><span class="box yb"></span><span class="n">No</span><span class="box nb"></span></div>
    <div class="row">Crooked teeth<span class="y">Yes</span><span class="box yb"></span><span class="n">No</span><span class="box nb"></span></div>
    <div class="row">Discoloured teeth<span class="y">Yes</span><span class="box yb"></span><span class="n">No</span><span class="box nb"></span></div>
    <div class="row">Sensitivity to Hot/Cold<span class="y">Yes</span><span class="box yb"></span><span class="n">No</span><span class="box nb"></span></div>
    <div class="row">Tooth pain when chewing<span class="y">Yes</span><span class="box yb"></span><span class="n">No</span><span class="box nb"></span></div>
    <div class="row">Jaw pain/Fracture<span class="y">Yes</span><span class="box yb"></span><span class="n">No</span><span class="box nb"></span></div>
    <div class="row">Orthodontic treatment/history<span class="y">Yes</span><span class="box yb"></span><span class="n">No</span><span class="box nb"></span></div>
    <div class="row">Oral Cancer<span class="y">Yes</span><span class="box yb"></span><span class="n">No</span><span class="box nb"></span></div>
  </div>

  <div class="group group--left" style="top:297px">
    <h3>Diet/Lifestyle</h3>
    <div class="row">Drink more than one<span class="y">Yes</span><span class="box yb"></span><span class="n">No</span><span class="box nb"></span></div>
    <div class="row">glass alcohol per day</div>
    <div class="row">Smoking<span class="y">Yes</span><span class="box yb"></span><span class="n">No</span><span class="box nb"></span></div>
    <div class="row">Carbonated drinks<span class="y">Yes</span><span class="box yb"></span><span class="n">No</span><span class="box nb"></span></div>
    <div class="row">Sugary foods<span class="y">Yes</span><span class="box yb"></span><span class="n">No</span><span class="box nb"></span></div>
  </div>

  <div class="group group--left" style="top:369px">
    <h3>Blood</h3>
    <div class="row">Anaemia<span class="y">Yes</span><span class="box yb"></span><span class="n">No</span><span class="box nb"></span></div>
    <div class="row">Blood clots<span class="y">Yes</span><span class="box yb"></span><span class="n">No</span><span class="box nb"></span></div>
    <div class="row">Leukemia<span class="y">Yes</span><span class="box yb"></span><span class="n">No</span><span class="box nb"></span></div>
    <div class="row">Low platelets<span class="y">Yes</span><span class="box yb"></span><span class="n">No</span><span class="box nb"></span></div>
    <div class="row">Lymphoma<span class="y">Yes</span><span class="box yb"></span><span class="n">No</span><span class="box nb"></span></div>
    <div class="row">Haemophelia<span class="y">Yes</span><span class="box yb"></span><span class="n">No</span><span class="box nb"></span></div>
  </div>

  <div class="group group--left" style="top:453px">
    <h3>Chest</h3>
    <div class="row">Bronchitis<span class="y">Yes</span><span class="box yb"></span><span class="n">No</span><span class="box nb"></span></div>
    <div class="row">Cystic Fibrosis<span class="y">Yes</span><span class="box yb"></span><span class="n">No</span><span class="box nb"></span></div>
    <div class="row">Emphysema<span class="y">Yes</span><span class="box yb"></span><span class="n">No</span><span class="box nb"></span></div>
    <div class="row">Pneumonia<span class="y">Yes</span><span class="box yb"></span><span class="n">No</span><span class="box nb"></span></div>
  </div>

  <div class="group group--left" style="top:515px">
    <h3>Infectious Disease</h3>
    <div class="row">Creutzfeldt-Jakob Disease<span class="y">Yes</span><span class="box yb"></span><span class="n">No</span><span class="box nb"></span></div>
    <div class="row">Hepatitis A,B,C,D<span class="y">Yes</span><span class="box yb"></span><span class="n">No</span><span class="box nb"></span></div>
    <div class="row">HIV/AIDS<span class="y">Yes</span><span class="box yb"></span><span class="n">No</span><span class="box nb"></span></div>
    <div class="row">Influenza<span class="y">Yes</span><span class="box yb"></span><span class="n">No</span><span class="box nb"></span></div>
    <div class="row">Shingles<span class="y">Yes</span><span class="box yb"></span><span class="n">No</span><span class="box nb"></span></div>
    <div class="row">Tuberculosis<span class="y">Yes</span><span class="box yb"></span><span class="n">No</span><span class="box nb"></span></div>
  </div>

  <div class="group group--right" style="top:101px">
    <h3>Heart</h3>
    <div class="row">Angina<span class="y">Yes</span><span class="box yb"></span><span class="n">No</span><span class="box nb"></span></div>
    <div class="row">Atrial Fibrillation<span class="y">Yes</span><span class="box yb"></span><span class="n">No</span><span class="box nb"></span></div>
    <div class="row">Blood Pressure (High/Low)<span class="y">Yes</span><span class="box yb"></span><span class="n">No</span><span class="box nb"></span></div>
    <div class="row">Congenital Heart Disease<span class="y">Yes</span><span class="box yb"></span><span class="n">No</span><span class="box nb"></span></div>
    <div class="row">Heart attack<span class="y">Yes</span><span class="box yb"></span><span class="n">No</span><span class="box nb"></span></div>
    <div class="row">Heart murmur<span class="y">Yes</span><span class="box yb"></span><span class="n">No</span><span class="box nb"></span></div>
    <div class="row">Heart surgery<span class="y">Yes</span><span class="box yb"></span><span class="n">No</span><span class="box nb"></span></div>
    <div class="row">Heart valve replacement<span class="y">Yes</span><span class="box yb"></span><span class="n">No</span><span class="box nb"></span></div>
    <div class="row">Infective endocarditis<span class="y">Yes</span><span class="box yb"></span><span class="n">No</span><span class="box nb"></span></div>
    <div class="row">Rheumatic Heart Disease<span class="y">Yes</span><span class="box yb"></span><span class="n">No</span><span class="box nb"></span></div>
    <div class="row">Pacemaker<span class="y">Yes</span><span class="box yb"></span><span class="n">No</span><span class="box nb"></span></div>
    <div class="row">Stent<span class="y">Yes</span><span class="box yb"></span><span class="n">No</span><span class="box nb"></span></div>
  </div>

  <div class="group group--right" style="top:249px">
    <h3>Other</h3>
    <div class="row">Anxiety/PTSD<span class="y">Yes</span><span class="box yb"></span><span class="n">No</span><span class="box nb"></span></div>
    <div class="row">Arthritis<span class="y">Yes</span><span class="box yb"></span><span class="n">No</span><span class="box nb"></span></div>
    <div class="row">Alzheimer's<span class="y">Yes</span><span class="box yb"></span><span class="n">No</span><span class="box nb"></span></div>
    <div class="row">Asthma<span class="y">Yes</span><span class="box yb"></span><span class="n">No</span><span class="box nb"></span></div>
    <div class="row">Anaphylaxis<span class="y">Yes</span><span class="box yb"></span><span class="n">No</span><span class="box nb"></span></div>
    <div class="row">Auto-immune disease<span class="y">Yes</span><span class="box yb"></span><span class="n">No</span><span class="box nb"></span></div>
    <div class="row">Coeliac<span class="y">Yes</span><span class="box yb"></span><span class="n">No</span><span class="box nb"></span></div>
    <div class="row">Depression<span class="y">Yes</span><span class="box yb"></span><span class="n">No</span><span class="box nb"></span></div>
    <div class="row">Diabetes<span class="y">Yes</span><span class="box yb"></span><span class="n">No</span><span class="box nb"></span></div>
    <div class="row">Epilepsy<span class="y">Yes</span><span class="box yb"></span><span class="n">No</span><span class="box nb"></span></div>
    <div class="row">Kidney Disease<span class="y">Yes</span><span class="box yb"></span><span class="n">No</span><span class="box nb"></span></div>
    <div class="row">Liver Disease<span class="y">Yes</span><span class="box yb"></span><span class="n">No</span><span class="box nb"></span></div>
    <div class="row">Osteoporosis<span class="y">Yes</span><span class="box yb"></span><span class="n">No</span><span class="box nb"></span></div>
    <div class="row">Parkinson's<span class="y">Yes</span><span class="box yb"></span><span class="n">No</span><span class="box nb"></span></div>
    <div class="row">Radiation to Head/Neck<span class="y">Yes</span><span class="box yb"></span><span class="n">No</span><span class="box nb"></span></div>
    <div class="row">Schizophrenia<span class="y">Yes</span><span class="box yb"></span><span class="n">No</span><span class="box nb"></span></div>
    <div class="row">Snoring<span class="y">Yes</span><span class="box yb"></span><span class="n">No</span><span class="box nb"></span></div>
    <div class="row">Sleep apnea<span class="y">Yes</span><span class="box yb"></span><span class="n">No</span><span class="box nb"></span></div>
    <div class="row">Stroke<span class="y">Yes</span><span class="box yb"></span><span class="n">No</span><span class="box nb"></span></div>
  </div>

  <div class="abs" style="left:270px;top:477px;width:188px"><div class="field">Other:<span class="line"></span></div></div>

  <div class="abs" style="left:20px;top:603px;width:251px"><div class="field">Signature:<span class="line"></span></div></div>
  <div class="abs" style="left:315px;top:603px;width:143px"><div class="field">Date:<span class="line"></span></div></div>

  <p class="thanks">Thank you for the time to complete your medical history form.<br>
    Oral health is linked to overall health and this comprehensive questionnaire will help us<br>
    to provide you with optimal and safe care.</p>

  <div class="band band--bottom"><span></span><span></span><span></span><span></span></div>
</section>

</body>
</html>
```